Luxury Face Oil Label

I'm looking for a simple and sophisticated design for a natural face oil that will target the luxe market. It is a pure Natural product. I have attached the logo, Velumi Organics.

Here's the Copy

LUXE FACIAL OIL

Regenerate. Hydrate. Glow

100% Natural

30ml (1.01 oz)

A complex blend of Pure Oils including Marula, Sea Buckthorn, Rosehip, Neroli, Evening primrose, Argan, Calendula, Lavender, Jojoba, Grapeseed, Baobab, Moringa and Vitamin E oil.

Produced by
Pellin Kettle Ltd
P.O box 7925-00300
Nairobi, Kenya
www.velumiorganics.example

Target Market(s)

High end

Requirements
Must have
• Simple, Please consider the bottle, which is a 30ml clear glass bottle with a gold and white pump. Image attached.
Nice to have
• Very clean designs, not too much going on.
Should not have
• Leaves and nuts.

```html
<!DOCTYPE html>
<html lang="en">
<head>
<meta charset="utf-8">
<title>Velumi Organics – Luxe Facial Oil Label</title>
<link rel="stylesheet" href="https://fonts.googleapis.com/css2?family=Mulish:wght@400;800&family=Questrial&display=swap">
<style>
  :root {
    --page: #fdfdfd;
    --label: #f3f6f0;
    --ink-dark: #3d4d33;
    --ink-light: #a8c48a;
    --line-soft: #dde7d2;
    --ink-black: #111111;
  }
  * { margin: 0; padding: 0; box-sizing: border-box; }
  html, body {
    width: 1200px; height: 1000px; overflow: hidden;
    background: var(--page);
  }
  .canvas { position: relative; width: 1200px; height: 1000px; }
  .label {
    position: absolute; left: 199px; top: 119px;
    width: 821px; height: 537px;
    background: var(--label);
  }
  .centered {
    position: absolute; transform: translateX(-50%);
    text-align: center; white-space: nowrap;
  }
  .brand-name {
    left: 203px; top: 180px;
    font-family: "Questrial", sans-serif;
    font-size: 19px; letter-spacing: 4px;
    color: var(--ink-dark);
  }
  .product-title {
    font-family: "Mulish", sans-serif; font-weight: 800;
    color: var(--ink-dark);
  }
  .front-title { left: 203px; top: 271px; font-size: 27px; }
  .natural-claim {
    left: 203px; top: 325px;
    font-family: "Mulish", sans-serif; font-weight: 800;
    font-size: 19px; color: var(--ink-light);
  }
  .benefits {
    left: 203px; top: 373px;
    font-family: "Questrial", sans-serif; font-size: 12.5px;
    color: var(--ink-dark);
    display: flex; align-items: center; gap: 16px;
  }
  .benefits .dot {
    width: 6px; height: 6px; border-radius: 50%;
    background: var(--ink-dark);
  }
  .volume {
    left: 202px; top: 485px;
    font-family: "Questrial", sans-serif; font-size: 13px;
    color: var(--ink-black);
  }
  .diamond-frame { position: absolute; left: 421px; top: 72px; }
  .back-title { left: 613px; top: 173px; font-size: 17px; }
  .ingredients {
    left: 613px; top: 227px;
    font-family: "Questrial", sans-serif; font-size: 15.5px;
    line-height: 17.4px; color: var(--ink-dark);
  }
  .producer {
    left: 605px; top: 488px;
    font-family: "Questrial", sans-serif; font-size: 10px;
    color: var(--ink-black);
  }
</style>
</head>
<body>
<div class="canvas">
  <section class="label">
    <p class="centered brand-name">VELUMI ORGANICS</p>

    <h1 class="centered product-title front-title">LUXE FACIAL OIL</h1>
    <p class="centered natural-claim">100% Natural</p>
    <p class="centered benefits">
      <span>Regenerate</span><span class="dot"></span>
      <span>Hydrate</span><span class="dot"></span>
      <span>Glow</span>
    </p>
    <p class="centered volume">30ml (1.01 oz)</p>

    <svg class="diamond-frame" width="380" height="380" viewBox="0 0 380 380" aria-hidden="true">
      <polygon points="190,2 378,190 190,378 2,190" fill="none" stroke="var(--line-soft)" stroke-width="1.2"/>
      <polygon points="190,11 369,190 190,369 11,190" fill="none" stroke="var(--line-soft)" stroke-width="2"/>
    </svg>

    <h2 class="centered product-title back-title">LUXE FACIAL OIL</h2>
    <p class="centered ingredients">
      A complex blend of Pure Oils<br>
      including Marula, Sea Buckthorn, Rose-<br>
      hip, Neroli, Evening primrose, Argan,<br>
      Calendula, Lavender, Jojoba, Grape-<br>
      seed, Baobab, Moringa and<br>
      Vitamin E oil.
    </p>
    <p class="centered producer">Produced by Pellin Kettle Ltd</p>
  </section>
</div>
</body>
</html>
```